Flyer Design Project - Financial services business specialising in mortgages and insurance

I require a flyer to create interest in saving money with mortgages. We show people that they can save money on their mortgages by paying the mortgage of sooner. Therefore they no longer need to work for the bank, and that they can live their life debt free.
The call to action is that they pick up the phone and call me or make an inquiry online via our website.

We are a insurance and mortgage brokerage and the business name is called BRAVO. Website: www.bravolenders.co.nz (currently)
the new website that isn't quite live yet is viewable at
www.qortasites.com/bravo

Our tag line is Hearth Growth Tomorrow

The type of clients we are trying to engage with are home owners with existing mortgages.

Aged between 35-40, Professionals, Income bracket of $80k plus for the household, in a relationship, no more than two kids, live in our local area (West Auckland, New Zealand) they are driven to be successful and have a comfortable family life and be able to afford luxuries.(responsible)

We would like to see what options someone can come up other than the ususal. Needs to fit with our business name BRAVO + Tag line. As in we do things BRAVOER.

The flyer needs to show that we can help make a difference.

We will provide a free comparative market report on their house for an appointment and also if we cant save the prospect any money our guarantee is that we will give them a $20 voucher. (conditions will apply).

Ideally looking to have the flyer on a DLE size although we are open to options.

more than happy to discuss further if required to. I have attached my logo and my current image for home loans used on the website although i would like to see if there are any better options available than my current image.

Reason: Waiting on a couple of other designers who were sending there designs through before closing of.

Target Market(s)

home owners with an existing mortgage. Ages between 35-40, Professionals, Income 80k+

Industry/Entity Type

Insurance

Requirements
Must have
• A disclosure document is available upon request.
Our logo and contact details.
Call to action
Nice to have
• Want to focus on the lifestyles and goals rather than the actual payment of the mortgage.
Should not have
• We don't want to be saying the same boring message as most mortgage brokers are saying ie. Call us we can save you thousands of dollars.
We a need a reason for them to call us to go with our image and brand.

```html
<!DOCTYPE html>
<html lang="en">
<head>
<meta charset="utf-8">
<title>BRAVO – Debt free lifestyle flyer</title>
<link rel="stylesheet" href="https://fonts.googleapis.com/css2?family=Arimo:wght@400;700&family=Roboto:wght@300&display=swap">
<style>
  :root {
    --navy: #0d3f66;
    --ink: #12324d;
    --orange: #f2a81d;
    --white: #ffffff;
    --brand-blue: #1470b8;
    --photo-deep: #1a6aab;
    --photo-mid: #3d8fcb;
    --photo-light: #a9d3ec;
    --band-top: #ffffff;
    --band-bottom: #cfe6f3;
  }
  html, body {
    margin: 0;
    padding: 0;
    overflow: hidden;
    background: #ffffff;
  }
  .flyer {
    position: relative;
    width: 1200px;
    height: 557px;
    overflow: hidden;
    font-family: "Arimo", Arial, sans-serif;
  }
  .lifestyle-photo {
    position: absolute;
    inset: 0;
    background: linear-gradient(100deg, var(--photo-deep) 0%, var(--photo-mid) 45%, var(--photo-light) 100%);
  }
  .band {
    position: absolute;
    inset: 0;
  }
  .headline {
    position: absolute;
    left: 48px;
    top: 18px;
    margin: 0;
    font-family: "Roboto", Arial, sans-serif;
    font-weight: 300;
    font-size: 84px;
    line-height: 1;
    color: var(--navy);
    letter-spacing: -0.5px;
    white-space: nowrap;
  }
  .subhead {
    position: absolute;
    left: 51px;
    top: 122px;
    margin: 0;
    font-weight: 700;
    font-size: 44px;
    line-height: 1;
    letter-spacing: 2.5px;
    color: var(--orange);
    white-space: nowrap;
  }
  .pitch {
    position: absolute;
    left: 51px;
    top: 181px;
    color: var(--white);
    font-size: 19px;
    line-height: 22px;
    white-space: nowrap;
  }
  .pitch p { margin: 0 0 21px; }
  .contact {
    position: absolute;
    left: 51px;
    top: 312px;
    color: var(--white);
    font-weight: 700;
    font-size: 27px;
    line-height: 37px;
    white-space: nowrap;
  }
  .more-info {
    position: absolute;
    left: 50px;
    top: 470px;
    margin: 0;
    color: var(--ink);
    font-size: 20px;
    white-space: nowrap;
  }
  .more-info strong {
    font-size: 27px;
    font-weight: 700;
  }
  .disclosure {
    position: absolute;
    left: 51px;
    top: 505px;
    margin: 0;
    color: var(--ink);
    font-size: 12.5px;
    white-space: nowrap;
  }
  .brand {
    position: absolute;
    right: 55px;
    top: 438px;
    color: var(--brand-blue);
    text-align: right;
  }
  .brand-name {
    display: block;
    font-weight: 700;
    font-size: 58px;
    line-height: 1;
    letter-spacing: 1px;
  }
  .brand-tagline {
    display: block;
    margin-top: 12px;
    font-size: 15px;
    font-weight: 400;
  }
</style>
</head>
<body>
  <div class="flyer">
    <div class="lifestyle-photo" role="img" aria-label="Photo of a woman in a sun hat relaxing in a beach chair with arms raised on a tropical beach"></div>

    <svg class="band" viewBox="0 0 1200 557" width="1200" height="557" aria-hidden="true">
      <defs>
        <linearGradient id="band-fill" x1="0" y1="0" x2="1" y2="1">
          <stop offset="0" stop-color="#ffffff"/>
          <stop offset="1" stop-color="#cfe6f3"/>
        </linearGradient>
      </defs>
      <path d="M0 458 Q560 380 1200 408 L1200 557 L0 557 Z" fill="url(#band-fill)"/>
      <path d="M0 446 Q560 362 1200 396 L1200 410 Q560 382 0 460 Z" fill="#f2a81d"/>
    </svg>

    <h1 class="headline">Want a Debt free lifestyle?</h1>
    <h2 class="subhead">WE CAN SHOW YOU HOW!</h2>

    <div class="pitch">
      <p>Talk to us about how you can pay your mortgage<br>off faster and take back control of your life.</p>
      <p>Call, text or email to make an appointment and<br>receive a <strong>FREE</strong> property report.</p>
    </div>

    <div class="contact">
      <div class="contact-phone">(09) 555 0142</div>
      <div class="contact-email">hello@bravolenders.co.nz</div>
    </div>

    <p class="more-info">For more info visit <strong>www.bravolenders.co.nz</strong></p>
    <p class="disclosure">A disclosure statement is available upon request.</p>

    <div class="brand">
      <span class="brand-name">BRAVO</span>
      <span class="brand-tagline">Hearth Growth Tomorrow</span>
    </div>
  </div>
</body>
</html>
```